Flyer for Dessert Cafe event launch

Hi
We are launching a new initiative at our cafe - this is the plan:
- We will open Saturday nights to serve desserts, tea and coffee and other after dinner deliciousness (no alcohol)
- Customers stop in and enjoy something sweets on the way home from dinner or movies. We'd decorate the garden with fairy lights, candles and lanterns and create a beautiful and relaxing (and romantic) after dinner atmosphere - maybe a little acoustic guitar
- For the menu we are thinking everything from chocolate mousse and cheesecake to tiramisu and dessert mocktails and even sorbet and gelato.
- The dessert cafe would probably trade from 7pm till 11pm.
Please check out www.brambelkitchen.com for our current branding feel.

We need an A4 flyer designed to promote this new venture.
I want the design to incorporate trees with fairy lights in them - and hearts - as we will be launching on Valentines Day evening (and the heart is part of our branding). Obviously the design needs to be tied in with our current branding - logo attached in various forms I am happy for you to use whichever fits best with your design. I have also attached some images that inspire me for this project - but they don't need to be used.

The following information will need to be included:

On the way home from dinner, or just craving something sweet?
Join us for Dessert!
Unwind - Relax - Indulge
7pm - 11pm every Saturday night
Starting on Valentines Day
All desserts handmade in-house - with love! *** Coffee *** Tea *** Mocktails *** Share platters available ***Gluten Free, Dairy Free and Vegan options *** Take-Away Available
Live Music

2248 Wattleridge Road, Kelvin Flats (five minutes from Marrowbay)
(03) 5391 8462
www.brambelkitchen.com
Please include the Facebook - Twiiter and Instagram Icons

```html
<!DOCTYPE html>
<html lang="en">
<head>
<meta charset="utf-8">
<title>Brambel Kitchen Café – Saturday Night Desserts</title>
<link rel="stylesheet" href="https://fonts.googleapis.com/css2?family=Lobster&family=Michroma&display=swap">
<style>
  :root {
    --rose: #d8265a;
    --rose-deep: #a8163f;
    --blush: #f7e4ec;
    --teal: #23889b;
    --teal-deep: #16606e;
    --white: #ffffff;
    --paper: #fdfafb;
    --dot-one: #36518f;
    --dot-two: #3aa5d8;
    --dot-three: #6b3d8c;
  }
  * { margin: 0; padding: 0; box-sizing: border-box; }
  html, body { width: 855px; height: 1200px; overflow: hidden; background: var(--paper); }
  .flyer { position: relative; width: 855px; height: 1200px; overflow: hidden; background: var(--paper); }

  .blossom-scene {
    position: absolute; left: 0; top: 0; width: 855px; height: 780px;
    background:
      radial-gradient(ellipse 320px 220px at 130px 110px, rgba(196,70,100,.75), transparent 70%),
      radial-gradient(ellipse 300px 200px at 720px 170px, rgba(226,110,140,.7), transparent 70%),
      radial-gradient(ellipse 260px 200px at 90px 420px, rgba(150,90,90,.55), transparent 70%),
      radial-gradient(ellipse 380px 220px at 650px 420px, rgba(240,170,190,.7), transparent 70%),
      linear-gradient(180deg, #e8a6b7 0%, #efc3cf 40%, #f6dde4 70%, rgba(253,250,251,0) 100%);
  }
  .dessert-photo {
    position: absolute; left: 140px; top: 760px; width: 715px; height: 440px;
    background:
      radial-gradient(ellipse 170px 130px at 480px 170px, rgba(214,100,140,.75), transparent 75%),
      radial-gradient(ellipse 90px 80px at 140px 120px, rgba(80,40,60,.55), transparent 75%),
      radial-gradient(ellipse 120px 90px at 270px 110px, rgba(222,90,80,.55), transparent 75%),
      radial-gradient(ellipse 380px 200px at 420px 230px, rgba(240,200,210,.6), transparent 75%);
  }

  .text { position: absolute; left: 0; width: 855px; text-align: center; white-space: nowrap; }

  .brand-name {
    top: 120px; font-family: "Lobster", cursive; font-size: 74px; color: var(--rose);
  }

  .teaser {
    top: 274px; font-family: "Lobster", cursive; font-size: 58px; line-height: 55px;
    color: var(--blush);
    text-shadow: 2px 3px 0 var(--rose-deep), 0 0 6px rgba(120,20,50,.4);
  }

  .caps { font-family: "Michroma", sans-serif; text-transform: uppercase; }
  .pink-caps {
    color: var(--rose); -webkit-text-stroke: 0.7px var(--rose);
    text-shadow: -1.5px -1.5px 0 var(--white), 1.5px -1.5px 0 var(--white),
                 -1.5px 1.5px 0 var(--white), 1.5px 1.5px 0 var(--white), 2px 3px 3px rgba(120,20,50,.45);
  }
  .teal-caps {
    color: var(--teal); -webkit-text-stroke: 0.7px var(--teal);
    text-shadow: -1.5px -1.5px 0 var(--white), 1.5px -1.5px 0 var(--white),
                 -1.5px 1.5px 0 var(--white), 1.5px 1.5px 0 var(--white), 2px 2px 0 rgba(216,38,90,.5);
  }

  .invite { top: 465px; font-size: 40px; line-height: 50px; }
  .mood { top: 516px; font-size: 28px; line-height: 34px; letter-spacing: 1px; }
  .details { top: 576px; font-size: 19px; line-height: 27px; }

  .drinks {
    top: 708px; font-family: "Lobster", cursive; font-size: 46px; line-height: 56px; color: var(--teal);
    text-shadow: 2px 2px 0 var(--white), 3px 3px 0 rgba(216,38,90,.5);
  }
  .offerings { top: 758px; font-size: 30px; line-height: 35px; }

  .contact { top: 986px; font-size: 17px; line-height: 22px; font-style: normal; }
  .web { top: 1049px; font-size: 23px; line-height: 30px; letter-spacing: 1px; }

  .social { top: 1102px; list-style: none; display: flex; flex-direction: column; align-items: center; }
  .social-item {
    display: flex; align-items: center; gap: 7px; height: 21px;
    font-family: "Michroma", sans-serif; font-size: 14px; text-transform: uppercase;
    color: var(--teal); -webkit-text-stroke: 0.4px var(--teal);
  }
  .social-dot { width: 19px; height: 19px; border-radius: 50%; flex: none; }
  .social-item.page .social-dot { background: var(--dot-one); }
  .social-item.feed .social-dot { background: var(--dot-two); }
  .social-item.gallery .social-dot { background: var(--dot-three); }
</style>
</head>
<body>
<main class="flyer">
  <div class="blossom-scene" role="img" aria-label="Soft-focus photograph of a pink blossom tree with fairy lights and floating hearts"></div>
  <div class="dessert-photo" role="img" aria-label="Close-up photograph of a raspberry cheesecake tart with berries and a mint leaf"></div>

  <div class="text brand-name">brambel kitchen café</div>

  <p class="text teaser">On the way home from dinner,<br>or just craving something<br>sweet?</p>

  <h1 class="text caps pink-caps invite">Join us for dessert!</h1>
  <p class="text caps pink-caps mood">Unwind - Relax - Indulge</p>
  <p class="text caps pink-caps details">7pm - 11pm every Saturday night<br>Starting on Valentines Day<br>All desserts handmade in-house -<br>with love!</p>

  <p class="text drinks">*** Coffee *** Tea *** Mocktails ***</p>
  <p class="text caps teal-caps offerings">Share platters available<br>Gluten free, dairy free and<br>vegan options<br>Take-away available<br>*** Live music ***</p>

  <address class="text caps pink-caps contact">2248 Wattleridge Road, Kelvin Flats<br>(five minutes from Marrowbay)<br>(03) 5391 8462</address>
  <p class="text caps pink-caps web">www.brambelkitchen.com</p>

  <ul class="text social">
    <li class="social-item page"><span class="social-dot"></span>www.friendwall.com/brambelkitchencafe</li>
    <li class="social-item feed"><span class="social-dot"></span>chirpline.com/brambelkitchen</li>
    <li class="social-item gallery"><span class="social-dot"></span>brambelkitchen</li>
  </ul>
</main>
</body>
</html>
```